Website Design For Atelier Nine Design Group

Create a sophisticated website that denotes high-end luxury. We would like to keep the copy minimalist and elegantly understated while communicating only the most essential information. While creating an air of exclusivity.
We would like 3-4 Tab Wesbite
Home:
• Feature a design project front and centre, along with a short
introduction about who we are and what we do.

We can put a Call To Action at the end of the introduction inviting readers to learn more on our About page.
About:
• This page should provide more detail on our background, past
achievements, history of the company, and anything you'd like to
highlight.
• We should also provide details on our services, aesthetic, process, etc.
Team:
• introduce the team, possibly with short descriptions for each
team member. Total Team Members 7
Residential
• The portfolio page can be a grid of images along with titles for
each project.
• Clicking on each image should take you to a separate page for that
project where readers can find more details

Commercial
The portfolio page can be a grid of images along with titles for
each project.

Contact Us:

example website:
https://www.morvexinteriors.example/

Target Market(s)

High end luxury clientele

Industry/Entity Type

Interior Design

Number of Pages Required

4 page

Font styles to use
Sans Serif

Requirements
Must have
• Company logo, color scheme and name: Atelier Nine Design Group

```html
<!DOCTYPE html>
<html lang="en">
<head>
<meta charset="UTF-8">
<title>Atelier Nine Design Group</title>
<link href="https://fonts.googleapis.com/css2?family=Teko:wght@400;500&family=Roboto:wght@400&display=swap" rel="stylesheet">
<style>
:root{
  --navy:#073444;
  --gold:#c9a240;
  --white:#ffffff;
  --mist:#f5f5f5;
  --ink:#222222;
  --display:"Teko", "Arial Narrow", sans-serif;
  --body:"Roboto", Arial, sans-serif;
}
*{margin:0;padding:0;box-sizing:border-box}
html,body{width:1200px;height:2836px;overflow:hidden;background:var(--white)}
.page{position:relative;width:1200px;height:2836px;font-family:var(--body);color:var(--ink)}

/* header */
.site-header{position:absolute;left:0;top:0;width:1200px;height:192px;background:var(--white)}
.brand{position:absolute;left:88px;top:62px;display:flex;align-items:center;gap:12px;font-family:var(--display);font-weight:500;font-size:40px;letter-spacing:2px;color:var(--navy);line-height:1}
.brand-square{width:20px;height:20px;background:var(--gold)}
.contact-item{position:absolute;top:34px;display:flex;align-items:center;gap:12px;font-family:var(--display);font-weight:500;font-size:25px;color:var(--navy);line-height:1;white-space:nowrap}
.contact-icon{width:36px;height:36px;border-radius:50%;background:var(--gold);display:flex;align-items:center;justify-content:center;flex:none}
.main-nav{position:absolute;top:110px;left:0;width:1200px}
.main-nav a{position:absolute;transform:translateX(-50%);font-family:var(--display);font-weight:500;font-size:24px;color:var(--navy);text-decoration:none;white-space:nowrap;line-height:1}
.main-nav a.active{color:var(--gold)}

/* hero */
.hero{position:absolute;left:0;top:192px;width:1200px;height:650px;background:linear-gradient(135deg,#7b807f 0%,#a9aca8 40%,#8c8e8a 70%,#6a6560 100%)}
.hero-title{position:absolute;left:0;top:235px;width:1200px;text-align:center;font-family:var(--display);font-weight:500;font-size:92px;line-height:1;color:var(--white);letter-spacing:1px}
.btn-solid{position:absolute;left:515px;top:351px;width:170px;height:51px;background:var(--gold);color:var(--white);font-family:var(--display);font-weight:500;font-size:28px;display:flex;align-items:center;justify-content:center;padding-top:4px}

/* intro sections */
.section-about{position:absolute;left:0;top:842px;width:1200px;height:852px;background:var(--white)}
.section-services{position:absolute;left:0;top:1694px;width:1200px;height:814px;background:var(--mist)}
.section-title{position:absolute;font-family:var(--display);font-weight:500;font-size:66px;line-height:1;color:var(--navy)}
.section-text{position:absolute;font-size:15px;line-height:22.5px;color:var(--ink)}
.btn-outline{position:absolute;width:163px;height:53px;border:2px solid var(--gold);color:var(--gold);font-family:var(--display);font-weight:500;font-size:30px;display:flex;align-items:center;justify-content:center;padding-top:4px}
.frame{position:absolute}
.photo{position:absolute}

/* footer */
.site-footer{position:absolute;left:0;top:2508px;width:1200px;height:328px;background:var(--navy)}
.footer-brand{position:absolute;left:0;top:78px;width:1200px;display:flex;justify-content:center;align-items:center;gap:12px;font-family:var(--display);font-weight:500;font-size:46px;letter-spacing:2px;color:var(--white);line-height:1}
.footer-nav a{position:absolute;top:193px;transform:translateX(-50%);font-family:var(--display);font-weight:500;font-size:23px;color:var(--white);text-decoration:none;white-space:nowrap;line-height:1}
.footer-rule{position:absolute;left:0;top:252px;width:1200px;height:1px;background:rgba(255,255,255,.25)}
.copyright{position:absolute;left:0;top:281px;width:1200px;text-align:center;font-size:13px;color:var(--white)}
</style>
</head>
<body>
<div class="page">

  <header class="site-header">
    <div class="brand"><span class="brand-square"></span>ATELIER NINE</div>

    <div class="contact-item" style="left:644px">
      <span class="contact-icon">
        <svg width="16" height="12" viewBox="0 0 16 12"><rect x="0.5" y="0.5" width="15" height="11" rx="1" fill="#fff"/><path d="M1 1.5 L8 7 L15 1.5" stroke="#c9a240" stroke-width="1.5" fill="none"/></svg>
      </span>
      info@ateliernine.example
    </div>
    <div class="contact-item" style="left:925px">
      <span class="contact-icon">
        <svg width="16" height="16" viewBox="0 0 24 24"><path fill="#fff" d="M6.6 10.8c1.4 2.8 3.8 5.1 6.6 6.6l2.2-2.2c.3-.3.7-.4 1-.2 1.1.4 2.3.6 3.6.6.6 0 1 .4 1 1V20c0 .6-.4 1-1 1C10.6 21 3 13.4 3 4c0-.6.4-1 1-1h3.5c.6 0 1 .4 1 1 0 1.3.2 2.5.6 3.6.1.3 0 .7-.2 1z"/></svg>
      </span>
      +555 014 2277
    </div>

    <nav class="main-nav">
      <a class="active" style="left:473px">HOME</a>
      <a style="left:566px">ABOUT</a>
      <a style="left:658px">TEAM</a>
      <a style="left:774px">RESIDENTIAL</a>
      <a style="left:916px">COMMERCIAL</a>
      <a style="left:1055px">CONTACT US</a>
    </nav>
  </header>

  <section class="hero" role="img" aria-label="Featured living room project with patterned curtains, sofa and coffee table">
    <h1 class="hero-title">ATELIER NINE DESIGN GROUP</h1>
    <div class="btn-solid">LEARN MORE</div>
  </section>

  <section class="section-about">
    <h2 class="section-title" style="left:101px;top:220px">WHO WE ARE</h2>
    <p class="section-text" style="left:102px;top:313px;width:414px">Lorem ipsum dolor sit amet, consectetur adipiscing elit, sed do eiusmod tempor incididunt ut labore et dolore magna aliqua. Ut enim ad minim veniam, quis nostrud exercitation ullamco laboris nisi ut aliquip ex ea commodo consequat. Duis aute irure dolor in reprehenderit in voluptate velit esse cillum dolore eu fugiat nulla pariatur. Excepteur sint occaecat cupidatat non proident, sunt in culpa qui officia deserunt mollit anim id est laborumSed ut perspiciatis unde.</p>
    <div class="btn-outline" style="left:102px;top:523px">LEARN MORE</div>

    <svg class="frame" style="left:627px;top:158px" width="386" height="506" viewBox="0 0 386 506">
      <path d="M0 0 H386 V26 H26 V480 H119 V506 H0 Z" fill="var(--gold)"/>
    </svg>
    <div class="photo" role="img" aria-label="Study with grey shelving, dark desk and upholstered armchair" style="left:653px;top:181px;width:445px;height:454px;background:linear-gradient(135deg,#5e6262 0%,#8a8c8a 45%,#cfcac0 75%,#6f7a76 100%)"></div>
  </section>

  <section class="section-services">
    <svg class="frame" style="left:92px;top:126px" width="389" height="473" viewBox="0 0 389 473">
      <path d="M0 0 H389 V27 H28 V446 H151 V473 H0 Z" fill="var(--navy)"/>
    </svg>
    <div class="photo" role="img" aria-label="Bathroom with marble walls, freestanding white tub and wooden side table" style="left:120px;top:153px;width:445px;height:418px;background:linear-gradient(135deg,#8d8f90 0%,#b4b5b5 45%,#e9eaeb 70%,#9a9793 100%)"></div>

    <h2 class="section-title" style="left:676px;top:181px">WHAT WE DO</h2>
    <p class="section-text" style="left:677px;top:266px;width:425px">Lorem ipsum dolor sit amet, consectetur adipiscing elit, sed do eiusmod tempor incididunt ut labore et dolore magna aliqua. Ut enim ad minim veniam, quis nostrud exercitation ullamco laboris nisi ut aliquip ex ea commodo consequat. Duis aute irure dolor in reprehenderit in voluptate velit esse cillum dolore eu fugiat nulla pariatur. Excepteur sint occaecat cupidatat non proident, sunt in culpa qui officia deserunt mollit anim id est laborumSed ut perspiciatis unde.</p>
    <div class="btn-outline" style="left:679px;top:466px">LEARN MORE</div>
  </section>

  <footer class="site-footer">
    <div class="footer-brand"><span class="brand-square"></span>ATELIER NINE</div>
    <nav class="footer-nav">
      <a style="left:338px">HOME</a>
      <a style="left:408px">ABOUT</a>
      <a style="left:484px">TEAM</a>
      <a style="left:587px">RESIDENTIAL</a>
      <a style="left:716px">COMMERCIAL</a>
      <a style="left:840px">CONTACT US</a>
    </nav>
    <div class="footer-rule"></div>
    <p class="copyright">© 2022&nbsp; ATELIER NINE DESIGN GROUP .ALL RIGHTS RESERVED</p>
  </footer>

</div>
</body>
</html>
```